QM Kalorvex.Brendal GmbH needed a letterhead template

For English scroll down. We need a letterhead template and since we already have our logo design successfully with you, we now want to also design the letterhead with you. Down in the uploaded file you see what is important and what should definitely be seen on our template. The template should be like the homepage (www.kalorvex.brendal) held in red, blue and white. We need a letter-head submission. In the bottom in the chapter "databases uploading" you can find the most important things, did must be on the submission. The submission shoulderstand be in the colors blue, red and white like our homepage (www.kalorvex.brendal).

```html
<!DOCTYPE html>
<html lang="de">
<head>
<meta charset="utf-8">
<title>QM Kalorvex.Brendal GmbH – Briefpapier</title>
<link href="https://fonts.googleapis.com/css2?family=Roboto+Condensed:wght@400&family=Roboto:wght@300&display=swap" rel="stylesheet">
<style>
  :root {
    --brand-blue: #0b62b4;
    --brand-red: #c42127;
    --paper: #ffffff;
    --backdrop: #e9e7e4;
    --on-color: #ffffff;
  }
  html, body {
    margin: 0;
    width: 1200px;
    height: 1200px;
    overflow: hidden;
    background: var(--backdrop);
  }
  .letterhead {
    position: absolute;
    left: 165px;
    top: 40px;
    width: 870px;
    height: 1120px;
    background: var(--paper);
    box-shadow: 0 2px 10px rgba(0,0,0,0.12);
    overflow: hidden;
  }
  .brand {
    position: absolute;
    left: 49px;
    top: 76px;
    display: flex;
    align-items: center;
    gap: 12px;
  }
  .brand-dot {
    width: 30px;
    height: 30px;
    border-radius: 50%;
    background: var(--brand-red);
  }
  .brand-name {
    font-family: "Roboto Condensed", sans-serif;
    font-weight: 400;
    font-size: 38px;
    color: var(--brand-blue);
    letter-spacing: 0.2px;
  }
  .address-tab {
    position: absolute;
    right: 0;
    top: 0;
    width: 279px;
    height: 149px;
  }
  .address-tab svg { position: absolute; inset: 0; }
  .address-tab .lines {
    position: absolute;
    right: 50px;
    top: 48px;
    text-align: right;
    font-family: "Roboto Condensed", sans-serif;
    font-size: 19px;
    line-height: 23.5px;
    color: var(--on-color);
  }
  .footer {
    position: absolute;
    left: 0;
    bottom: 0;
    width: 870px;
    height: 121px;
    background: var(--brand-red);
    color: var(--on-color);
    font-family: "Roboto", sans-serif;
    font-weight: 300;
    font-size: 13.5px;
    line-height: 17px;
  }
  .footer-col {
    position: absolute;
    text-align: center;
    transform: translateX(-50%);
    white-space: nowrap;
  }
  .col-company { left: 157px; top: 8px; }
  .col-contact { left: 449px; top: 16px; }
  .col-bank { left: 726px; top: 8px; }
  .footer-divider {
    position: absolute;
    top: 15px;
    width: 1px;
    height: 51px;
    background: var(--on-color);
  }
  .divider-one { left: 311px; }
  .divider-two { left: 587px; }
</style>
</head>
<body>
  <main class="letterhead">
    <header>
      <div class="brand">
        <span class="brand-dot"></span>
        <span class="brand-name">Kalorvex.Brendal</span>
      </div>
      <div class="address-tab">
        <svg width="279" height="149" viewBox="0 0 279 149">
          <polygon points="62,0 279,0 279,149 62,149 0,75" fill="var(--brand-blue)"/>
        </svg>
        <div class="lines">
          QM Kalorvex.Brendal GmbH<br>
          Moosgasse 4<br>
          6287 Felbrunn, Brendal<br>
          Österreich
        </div>
      </div>
    </header>
    <footer class="footer">
      <div class="footer-col col-company">
        Geschäftsführer Dr. Lindqvar Emil<br>
        Moosgasse 4<br>
        6287 Felbrunn, Brendal<br>
        Österreich
      </div>
      <span class="footer-divider divider-one"></span>
      <div class="footer-col col-contact">
        Telefon : 0800 XX XX XX<br>
        Mail : contact@kalorvex.brendal<br>
        Web : www.kalorvex.brendal
      </div>
      <span class="footer-divider divider-two"></span>
      <div class="footer-col col-bank">
        Vellmar Bank XXXX<br>
        IBAN : ATXX XXXX XXXX XXXX<br>
        BIC : XXXX<br>
        UID-Nr : ATUXXXXXX
      </div>
    </footer>
  </main>
</body>
</html>
```